Hotel Business Card Project

Amber Crest Hotel will be a premium boutique hotel in Dhaka, Bangladesh. The hotel will offer the finest amenities and facilities available on the market, and the cost per room investment will far exceed other 5-star hotels currently in the market.

As a result, we wanted the business card to reflect that premium/luxurious/upscale feel, and also be elegant and hospitable at the same time.

The name 'Amber Crest' is derived from the fact that Bangladesh has 6 distinct seasons (you can get more information online if required, or contact me about it). The leaves in the logo has the tree because trees give people shade, protection and safety (just like our hotel would try to give).

Target Market(s)

Business professionals, guests

Industry/Entity Type

Investment

Requirements
Must have
• Elegant, Classy and very attractive business card.

Must be editable to enter specific Names, Positions, Phone numbers and email later on.
Nice to have
• The address would be: House 47, Road 23, Lakeview 5, Dhaka 1208, Bangladesh

Slogan- Luxury Redefined

```html
<!DOCTYPE html>
<html lang="en">
<head>
<meta charset="UTF-8">
<title>Amber Crest Hotel – Business Card</title>
<link href="https://fonts.googleapis.com/css2?family=Source+Sans+3:wght@400;600&display=swap" rel="stylesheet">
<style>
  :root {
    --backdrop-light: #f2f2f2;
    --backdrop-dark: #d6d7d9;
    --card-white: #ffffff;
    --card-gold: #c49b33;
    --band-edge: #a9793c;
    --band-mid: #dcc08a;
    --band-light: #f4e8bb;
    --rule-gold: #d2ad5e;
    --text-brown: #9c6f32;
    --text-grey: #6a6a6a;
    --label-gold: #c8952a;
    --name-grey: #6b6b6b;
  }
  * { margin: 0; padding: 0; box-sizing: border-box; }
  html, body { width: 1200px; height: 901px; overflow: hidden; }
  body {
    position: relative;
    font-family: "Source Sans 3", "Myriad Pro", Arial, sans-serif;
    background: radial-gradient(ellipse at 50% 40%, var(--backdrop-light) 0%, var(--backdrop-dark) 100%);
  }
  .card {
    position: absolute;
    left: 281px;
    width: 637px;
    height: 389px;
    box-shadow: 4px 5px 8px rgba(0,0,0,0.35);
  }
  .card--front { top: 34px; background: var(--card-white); }
  .card--back { top: 455px; background: var(--card-gold); }

  .gold-band {
    position: absolute;
    left: 0; right: 0;
    background: linear-gradient(90deg, var(--band-edge) 0%, var(--band-mid) 22%, var(--band-light) 50%, var(--band-mid) 78%, var(--band-edge) 100%);
    display: flex;
    flex-direction: column;
    align-items: center;
    justify-content: center;
  }
  .gold-rule {
    position: absolute;
    left: 0; right: 0;
    height: 1.5px;
    background: var(--rule-gold);
  }

  .brand {
    position: absolute;
    top: 120px;
    left: 0; right: 0;
    display: flex;
    align-items: center;
    justify-content: center;
    gap: 14px;
  }
  .brand__dot {
    width: 22px; height: 22px;
    border-radius: 50%;
    background: var(--label-gold);
  }
  .brand__name {
    font-size: 34px;
    font-weight: 400;
    color: var(--name-grey);
    letter-spacing: 0.5px;
  }

  .card--front .gold-band { top: 245px; height: 40px; }
  .rule-top { top: 238px; }
  .rule-bottom { top: 289px; }
  .tagline {
    font-size: 21px;
    color: var(--text-brown);
    letter-spacing: 0.6px;
  }

  .contact { position: absolute; left: 0; right: 0; text-align: center; color: var(--text-grey); }
  .contact__address { top: 332px; font-size: 17.5px; letter-spacing: 0.4px; }
  .contact__lines { top: 357px; font-size: 14.5px; }
  .contact__label { color: var(--label-gold); font-weight: 600; margin-left: 6px; }
  .contact__label:first-child { margin-left: 0; }

  .card--back .gold-band { top: 150px; height: 78px; }
  .person__name { font-size: 23px; color: var(--text-brown); line-height: 1; }
  .person__role { font-size: 14px; color: var(--text-brown); letter-spacing: 2.6px; margin-top: 3px; }
</style>
</head>
<body>
  <section class="card card--front">
    <div class="brand">
      <span class="brand__dot"></span>
      <span class="brand__name">Amber Crest Hotel</span>
    </div>
    <div class="gold-rule rule-top"></div>
    <div class="gold-band"><p class="tagline">Luxury Redefined</p></div>
    <div class="gold-rule rule-bottom"></div>
    <p class="contact contact__address">House 47, Road 23, Lakeview 5, Dhaka 1208, Bangladesh</p>
    <p class="contact contact__lines">
      <span class="contact__label">T:</span> 6780 214365
      <span class="contact__label">F:</span> 6780 365214
      <span class="contact__label">E:</span> stay@ambercrest.com
      <span class="contact__label">W:</span> ambercresthotel.com
    </p>
  </section>

  <section class="card card--back">
    <div class="gold-band">
      <p class="person__name">Rafiq Ahmed</p>
      <p class="person__role">MANAGER</p>
    </div>
  </section>
</body>
</html>
```